Website for Company to help with House Restoration from Hurricane Damage

Crisp, Clean and Professional!

I need a FRONT page for a website. I need it created in photoshop with the layers intact. We DO NOT need the HTML or RBT for the site. Simply the design. Any fonts you use will need to be included if they are not standard. Please make sure any fonts you use in the body of the text are available for use on Google Fonts.

I have attached a word doc that lists the menu items and additional instructions.

A little about the company - after Hurricane Quintessa - RBT developed a system which allows the house to be raised, the Pylonets installed, and the house reset on the Pylonets without the expense of moving the house or driving new pilings. This option can be installed in a matter of days with limited space and at a lower construction cost.

Please refer to the attached musthaves.doc and images that are included.

The main page must incorporate the menu, the attached photos w/ text underneath (text is in the word doc attached), and the text included in the word doc.

Standard footer with contact info as well.

If you have questions please contact us!
Updates

Designs are due by Friday! We will pick one this weekend.  We are unable to change it from 10 days to 5.  Thank you!!!

Target Market(s)

People who lost their homes or businesses due to a hurricane.

Industry/Entity Type

Construction

Requirements
Must have
• See attached musthaves.doc

```html
<!DOCTYPE html>
<html lang="en">
<head>
<meta charset="utf-8">
<title>RBT – Rebuild Safer, Stronger, Better</title>
<link href="https://fonts.googleapis.com/css2?family=Open+Sans:wght@400;600&display=swap" rel="stylesheet">
<style>
:root{
  --bg-top:#788f4e;
  --bg-bottom:#dfe9c4;
  --white:#ffffff;
  --nav:#7a8c55;
  --nav-active:#a6b785;
  --accent:#6f8446;
  --footer:#5e6e3f;
  --footer-dark:#3d4a28;
  --footer-text:#e9eedb;
  --body-text:#222222;
  --muted-text:#333333;
}
*{margin:0;padding:0;box-sizing:border-box}
html,body{width:1200px;height:949px;overflow:hidden}
body{background:linear-gradient(180deg,var(--bg-top) 0%,#a9bd82 55%,var(--bg-bottom) 100%);font-family:"Open Sans",Arial,sans-serif}
.stage{position:absolute;left:0;top:0;width:1400px;height:1107px;transform:scale(0.857142857);transform-origin:0 0}
.page{position:absolute;left:200px;top:25px;width:1000px;height:1035px;background:var(--white);border-radius:8px;overflow:hidden}
.brand{position:absolute;left:21px;top:38px;display:flex;align-items:center;gap:8px;font-size:40px;font-weight:600;color:var(--accent)}
.brand-dot{width:18px;height:18px;border-radius:50%;background:var(--nav-active)}
.contact-bar{position:absolute;right:21px;top:24px;display:flex;align-items:center;gap:30px;font-size:14px;color:var(--muted-text)}
.contact-item{display:flex;align-items:center;gap:8px}
.main-nav{position:absolute;left:194px;top:71px;width:786px;height:53px;background:var(--nav);border-radius:5px;display:flex;align-items:stretch;overflow:hidden}
.main-nav a{color:var(--white);text-decoration:none;font-size:14px;text-transform:uppercase;display:flex;align-items:center;padding:0 14.5px;position:relative}
.main-nav a+a::before{content:"";position:absolute;left:0;top:19px;height:16px;width:1px;background:rgba(255,255,255,.45)}
.main-nav a.active{background:var(--nav-active);padding:0 16px 0 17px}
.main-nav a.active+a::before{display:none}
.hero{position:absolute;left:21px;top:146px;width:958px;height:399px;background:linear-gradient(180deg,#b9a7b4 0%,#e8b59a 30%,#b08e8a 48%,#6f6d7e 62%,#8b8ea0 78%,#aeb0bd 100%)}
.hero-caption{position:absolute;left:76px;top:161px}
.hero-caption span{display:inline-block;background:var(--accent);color:var(--white);font-size:18px;font-weight:600;padding:1px 9px 2px;line-height:26px;margin-bottom:9px}
.hero-arrow{position:absolute;top:159px}
.hero-arrow.prev{left:16px}
.hero-arrow.next{right:18px}
.intro-photo{position:absolute;left:21px;top:567px;width:297px;height:283px;background:radial-gradient(ellipse at 50% 55%,#c9c2b6 0%,#e6e2dc 55%,#f1efec 100%)}
.intro-text{position:absolute;left:337px;top:564px;width:644px;font-size:13px;line-height:18px;color:var(--body-text)}
.intro-text p+p{margin-top:12px}
.read-more{position:absolute;left:858px;top:817px;width:120px;height:34px;background:var(--accent);color:var(--white);font-size:13px;border-radius:4px;display:flex;align-items:center;justify-content:center;text-decoration:none}
.site-footer{position:absolute;left:0;top:895px;width:1000px;height:88px;background:var(--footer);color:var(--footer-text);text-align:center;font-size:14px;line-height:20px;padding-top:18px}
.footer-bar{position:absolute;left:0;top:983px;width:1000px;height:52px;background:var(--footer-dark);color:var(--footer-text);font-size:14px;display:flex;align-items:center;justify-content:space-between;padding:0 21px}
.footer-links a{color:var(--footer-text);text-decoration:none}
.footer-links .sep{margin:0 11px}
</style>
</head>
<body>
<div class="stage">
  <div class="page">
    <div class="brand"><span class="brand-dot"></span>RBT</div>

    <div class="contact-bar">
      <div class="contact-item">
        <svg width="18" height="26" viewBox="0 0 18 26"><rect x="1" y="4" width="16" height="21" rx="2" fill="#7a8c55"/><rect x="12" y="0" width="3" height="5" fill="#7a8c55"/><rect x="4" y="7" width="10" height="5" fill="#fff"/><g fill="#fff"><rect x="4" y="14" width="2.5" height="2"/><rect x="8" y="14" width="2.5" height="2"/><rect x="12" y="14" width="2" height="2"/><rect x="4" y="18" width="2.5" height="2"/><rect x="8" y="18" width="2.5" height="2"/><rect x="12" y="18" width="2" height="2"/></g></svg>
        <span>18004-0210</span>
      </div>
      <div class="contact-item">
        <svg width="28" height="18" viewBox="0 0 28 18"><rect x="0" y="0" width="28" height="18" rx="1" fill="#7a8c55"/><path d="M1 1 L14 11 L27 1" fill="none" stroke="#fff" stroke-width="1.6"/><path d="M1 17 L10 8 M27 17 L18 8" stroke="#fff" stroke-width="1.2"/></svg>
        <span>SALES@REBUILDBEARING.COM</span>
      </div>
    </div>

    <nav class="main-nav">
      <a class="active" href="#">Home</a>
      <a href="#">Services</a>
      <a href="#">About Us</a>
      <a href="#">Product Specifications</a>
      <a href="#">Design Documentation</a>
      <a href="#">Contact Us</a>
    </nav>

    <div class="hero" role="img" aria-label="Photo: a father and toddler reaching for each other on a sandy beach at sunset, boats on the bay behind them">
      <div class="hero-caption">
        <span>REBUILD SAFER, STRONGER, BETTER TO</span><br>
        <span>BUILD NEW LASTING MEMORIES</span>
      </div>
      <svg class="hero-arrow prev" width="36" height="82" viewBox="0 0 36 82"><path d="M34 1 L2 41 L34 81" fill="none" stroke="#fff" stroke-width="2" opacity=".8"/></svg>
      <svg class="hero-arrow next" width="36" height="82" viewBox="0 0 36 82"><path d="M2 1 L34 41 L2 81" fill="none" stroke="#fff" stroke-width="2" opacity=".8"/></svg>
    </div>

    <div class="intro-photo" role="img" aria-label="Photo: cupped hands holding a small model house with a green roof"></div>

    <div class="intro-text">
      <p>Systems for extending the height of existing piles are not available on today’s market. Rebuild Bearing Technologies, LLC (RBT) has developed two systems to allow for Piles to be extended that provide superior structural support without corrosion and maintenance concerns. We provided two systems, a complete system, Pile Cap Extension Pylonets, and Pile Splice. These two systems allow a home to be raised to by up to 54”, higher extensions possible with additional design consideration for lateral support. Shown below is the full Piling Extension system, which connects to the top of the existing pile. The system modular and can be cut to meet specific needs of the home.</p>
      <p>Our Patented Piling system has been designed to withstand the corrosive environment of beach communities. The salt water and windblown sand corrodes unprotected materials, and yes, even stainless steel. Our system utilizes a high strength carbon fiber material that is corrosion proof from salt water and UV proof. The system will not erode, decay or loose strength over time. The system has three installation conditions, for raising a house on existing pilings, repairing damaged pilings, and for connecting new pilings to floor joists in new construction. The three options are generally described here</p>
    </div>
    <a class="read-more" href="#">READ MORE</a>

    <footer class="site-footer">
      Rebuild Bearing Technologies, LLC - PO Box 31420,&nbsp; Maple Grove, PA 18004-0210 -(610) 555-0148<br>
      Email: sales@rebuildbearing.com
    </footer>
    <div class="footer-bar">
      <span>Copyright © 2013 RBT</span>
      <span class="footer-links">
        <a href="#">Home</a><span class="sep">|</span><a href="#">Service</a><span class="sep">|</span><a href="#">About Us</a><span class="sep">|</span><a href="#">Product Specifications</a><span class="sep">|</span><a href="#">Design Documentation</a><span class="sep">|</span><a href="#">Contact Us</a>
      </span>
    </div>
  </div>
</div>
</body>
</html>
```